Harborline Energy - needs a business card

Harborline Energy is a U.S. based diesel sourcing and distribution company that supports American oil & gas fields through providing quality product and consistent services.

Target Market(s)

Oil and Gas

Contact Information for Business Card

The background of the card must be white to ensure the logo pops.

Font styles to use
Serif
Sans Serif

Colors

Designer to choose colors to be used in the design.

Requirements
Must have
• Front of Card: Tag line: Harborline Energy, Powering America's Oil & Gas fields.
• Not sure if you guys do this part but just in case...
• Dale Menschow
• Owner/CEO
• C:555.318.4076
• E:Dmenschow@harborlineenergy.example
• W:Harborlineenergy.example
• Locations: Servicing the Powder River, DJ basin and Bakken formations.
• Back of Card: " Frac fueling is what we do. We understand how important diesel fuel is to your operation, which is why our main service line is Frac fueling. We assure our supply and stand by our service"

```html
<!DOCTYPE html>
<html lang="en">
<head>
<meta charset="utf-8">
<title>Harborline Energy – Business Card</title>
<link rel="stylesheet" href="https://fonts.googleapis.com/css2?family=Montserrat:wght@600;700&family=Raleway:wght@400;500&family=Lato:ital,wght@1,400&display=swap">
<style>
  :root {
    --navy: #1b2d5e;
    --red: #c0202a;
    --paper: #f7f7f5;
    --grey: #8a8d93;
    --ink-soft: #6c7079;
    --band-text: #8c9bc2;
    --backdrop: #d9d9d7;
  }
  * { box-sizing: border-box; margin: 0; padding: 0; }
  html, body { width: 1200px; height: 1200px; overflow: hidden; }
  body {
    background: var(--backdrop);
    display: flex;
    flex-direction: column;
    align-items: center;
    justify-content: center;
    gap: 60px;
  }
  .card {
    position: relative;
    width: 840px;
    height: 480px;
    overflow: hidden;
    box-shadow: 0 8px 24px rgba(0,0,0,0.18);
  }

  /* Front */
  .card-front { background: var(--paper); }
  .brand {
    position: absolute;
    left: 0; top: 0;
    width: 360px; height: 412px;
    display: flex; flex-direction: column;
    align-items: center; justify-content: center;
    gap: 18px;
    padding: 0 24px;
  }
  .brand-mark {
    width: 90px; height: 90px; border-radius: 50%;
    background: var(--navy);
  }
  .brand-name {
    font-family: "Montserrat", sans-serif;
    font-weight: 700;
    font-size: 36px;
    letter-spacing: 1px;
    color: var(--navy);
    text-transform: uppercase;
    text-align: center;
    line-height: 1.1;
  }
  .tagline {
    font-family: "Raleway", sans-serif;
    font-size: 14px;
    line-height: 1.35;
    letter-spacing: 0.3px;
    color: var(--ink-soft);
    text-align: center;
    max-width: 290px;
  }
  .divider {
    position: absolute;
    left: 360px; top: 70px;
    width: 3px; height: 300px;
    background: var(--navy);
  }
  .contact {
    position: absolute;
    left: 395px; top: 70px;
    right: 24px;
  }
  .person-name {
    font-family: "Montserrat", sans-serif;
    font-weight: 700;
    font-size: 30px;
    letter-spacing: 1px;
    text-transform: uppercase;
    color: var(--navy);
  }
  .person-name .surname { color: var(--red); }
  .person-role {
    font-family: "Raleway", sans-serif;
    font-size: 22px;
    color: var(--grey);
    letter-spacing: 1px;
    margin-top: 2px;
  }
  .contact-list { list-style: none; margin-top: 44px; }
  .contact-list li {
    display: flex; align-items: center; gap: 14px;
    font-family: "Raleway", sans-serif;
    font-weight: 500;
    font-size: 17px;
    letter-spacing: 0.5px;
    color: var(--ink-soft);
    height: 34px;
    white-space: nowrap;
  }
  .contact-list svg { width: 20px; height: 20px; flex: none; }
  .locations {
    position: absolute;
    left: 0; bottom: 0;
    width: 100%; height: 68px;
    background: var(--navy);
    display: flex; align-items: center;
    padding-left: 40px;
    font-family: "Raleway", sans-serif;
    font-size: 20px;
    letter-spacing: 1px;
    color: var(--band-text);
  }

  /* Back */
  .card-back {
    background: var(--navy);
    display: flex; flex-direction: column;
    align-items: center; justify-content: center;
    gap: 18px;
    padding: 0 90px;
  }
  .card-back .brand-mark { background: #ffffff; width: 84px; height: 84px; }
  .card-back .brand-name { color: #ffffff; font-size: 34px; }
  .mission {
    margin-top: 14px;
    font-family: "Lato", sans-serif;
    font-style: italic;
    font-size: 19px;
    line-height: 1.45;
    color: #ffffff;
    text-align: center;
  }
</style>
</head>
<body>

  <section class="card card-front" aria-label="Business card front">
    <div class="brand">
      <div class="brand-mark"></div>
      <div class="brand-name">Harborline<br>Energy</div>
      <p class="tagline">Harborline Energy, Powering America's Oil &amp; Gas fields.</p>
    </div>
    <div class="divider"></div>
    <div class="contact">
      <h1 class="person-name">Dale <span class="surname">Menschow</span></h1>
      <p class="person-role">Owner/CEO</p>
      <ul class="contact-list">
        <li>
          <svg viewBox="0 0 24 24" aria-hidden="true"><path fill="#8a8d93" d="M6.6 10.8a15.2 15.2 0 0 0 6.6 6.6l2.2-2.2c.3-.3.7-.4 1-.2 1.1.4 2.3.6 3.6.6.6 0 1 .4 1 1V20c0 .6-.4 1-1 1A17 17 0 0 1 3 4c0-.6.4-1 1-1h3.5c.6 0 1 .4 1 1 0 1.3.2 2.5.6 3.6.1.3 0 .7-.2 1z"/></svg>
          555.318.4076
        </li>
        <li>
          <svg viewBox="0 0 24 24" aria-hidden="true"><rect x="2.5" y="5" width="19" height="14" fill="none" stroke="#8a8d93" stroke-width="1.8"/><path d="M2.5 5l9.5 8 9.5-8" fill="none" stroke="#8a8d93" stroke-width="1.8"/></svg>
          Dmenschow@harborlineenergy.example
        </li>
        <li>
          <svg viewBox="0 0 24 24" aria-hidden="true"><g fill="none" stroke="#8a8d93" stroke-width="1.6"><circle cx="12" cy="12" r="9.5"/><ellipse cx="12" cy="12" rx="4" ry="9.5"/><path d="M2.5 12h19M4 7h16M4 17h16"/></g></svg>
          Harborlineenergy.example
        </li>
      </ul>
    </div>
    <div class="locations">Servicing the Powder River, DJ basin and Bakken formations</div>
  </section>

  <section class="card card-back" aria-label="Business card back">
    <div class="brand-mark"></div>
    <div class="brand-name">Harborline Energy</div>
    <p class="mission">“ Frac fueling is what we do. We understand how important diesel fuel is to your operation, which is why our main service line is Frac fueling. We assure our supply and stand by our service”</p>
  </section>

</body>
</html>
```